Floor Inspections and Consulting

We provide inspections and consulting services on various floor coverings, e.g. carpet, hardwood, etc. We also do expert witness work for attorneys due to floor covering failures. We current have a logo, just need it incorporated into a new design. I have examples of cards I have found on the internet that capture my attention and make a statement. I have included our original business card, which in my opinion is terrible, but it does have our logo on it.

```html
<!DOCTYPE html>
<html lang="en">
<head>
<meta charset="utf-8">
<title>Crestline Floor Inspections – Business Card</title>
<link rel="stylesheet" href="https://fonts.googleapis.com/css2?family=Open+Sans:wght@400;600;700&display=swap">
<style>
  :root {
    --page-bg: #c4c4c3;
    --navy: #0a4aa0;
    --cyan: #05a8d8;
    --silver: #d9dde2;
    --silver-dark: #8c949c;
    --white: #ffffff;
    --ink: #1a1a1a;
  }
  * { box-sizing: border-box; margin: 0; padding: 0; }
  html, body {
    width: 1200px; height: 900px; overflow: hidden;
    background: var(--page-bg);
    font-family: "Open Sans", Arial, sans-serif;
  }
  .sheet {
    position: relative; width: 1200px; height: 900px;
    display: flex; flex-direction: column; align-items: center; justify-content: center; gap: 60px;
  }
  .card {
    position: relative; width: 630px; height: 360px; overflow: hidden;
    box-shadow: 0 6px 18px rgba(0,0,0,0.18);
  }
  .card-art { position: absolute; inset: 0; width: 100%; height: 100%; }

  .brand {
    position: absolute; display: flex; align-items: center; gap: 12px;
    font-weight: 700; font-size: 22px; line-height: 1.15; letter-spacing: 0.5px;
    text-transform: uppercase;
  }
  .brand-dot { width: 34px; height: 34px; border-radius: 50%; flex: none; }

  /* front */
  .card-front .brand { left: 34px; top: 52px; color: var(--navy); }
  .card-front .brand-dot { background: var(--navy); }
  .card-front .tagline {
    position: absolute; left: 34px; top: 150px;
    font-size: 13px; letter-spacing: 1px; color: var(--ink);
  }
  .credentials {
    position: absolute; right: 30px; top: 40px; text-align: right;
    color: var(--white); font-size: 14px; letter-spacing: 1px; line-height: 1.5;
  }
  .contact {
    position: absolute; right: 30px; bottom: 26px; text-align: right; color: var(--white);
  }
  .contact-name { font-size: 28px; font-weight: 700; letter-spacing: 1px; margin-bottom: 8px; }
  .contact-line {
    display: flex; justify-content: flex-end; align-items: center; gap: 8px;
    font-size: 14px; line-height: 1.6;
  }
  .contact-line.phone { font-size: 19px; }
  .contact-line svg { width: 14px; height: 14px; flex: none; }
  .contact-line.phone svg { width: 17px; height: 17px; }

  /* back */
  .card-back .brand { left: 200px; top: 110px; color: var(--white); }
  .card-back .brand-dot { background: var(--white); }
  .card-back .tagline {
    position: absolute; left: 300px; top: 205px;
    font-size: 13px; letter-spacing: 1px; color: var(--white);
  }
</style>
</head>
<body>
<main class="sheet">

  <section class="card card-front" aria-label="Business card front">
    <svg class="card-art" viewBox="0 0 630 360" preserveAspectRatio="none" aria-hidden="true">
      <rect width="630" height="360" fill="var(--white)"/>
      <path d="M365,0 H630 V360 H300 C288,240 300,110 365,0 Z" fill="var(--navy)"/>
      <path d="M0,360 V286 Q300,120 630,205 V360 Z" fill="var(--cyan)"/>
      <path d="M0,280 Q300,114 630,199" fill="none" stroke="var(--navy)" stroke-width="3"/>
      <path d="M0,286 Q300,120 630,205" fill="none" stroke="var(--silver)" stroke-width="6"/>
      <path d="M0,290 Q300,124 630,209" fill="none" stroke="var(--silver-dark)" stroke-width="1.2" opacity="0.6"/>
    </svg>

    <div class="brand"><span class="brand-dot"></span><span>Crestline Floor<br>Inspections</span></div>
    <p class="tagline">ANALYSIS &amp; CONSULTING</p>

    <p class="credentials">CERTIFIED FLOOR COVERING<br>INSPECTIONS &amp; CONSULTING</p>

    <div class="contact">
      <p class="contact-name">DANIEL MARSH</p>
      <p class="contact-line phone">
        <svg viewBox="0 0 24 24" fill="none" stroke="currentColor" stroke-width="2"><circle cx="12" cy="12" r="10"/><path d="M9 7c-1 1-1 3 1 6s4 4 5 3l1-1-2-2-1 1c-1-.5-2-1.5-2.5-2.5l1-1-2-2z" fill="currentColor" stroke="none"/></svg>
        <span>303-555-0142</span>
      </p>
      <p class="contact-line">
        <svg viewBox="0 0 24 24" fill="none" stroke="currentColor" stroke-width="2"><rect x="3" y="6" width="18" height="12"/><path d="M3 6l9 7 9-7"/></svg>
        <span>dan@crestlinefloors.com</span>
      </p>
      <p class="contact-line">
        <svg viewBox="0 0 24 24" fill="none" stroke="currentColor" stroke-width="2"><circle cx="12" cy="12" r="9"/><path d="M3 12h18M12 3c3 3 3 15 0 18M12 3c-3 3-3 15 0 18"/></svg>
        <span>crestlinefloors.com</span>
      </p>
    </div>
  </section>

  <section class="card card-back" aria-label="Business card back">
    <svg class="card-art" viewBox="0 0 630 360" preserveAspectRatio="none" aria-hidden="true">
      <rect width="630" height="360" fill="var(--navy)"/>
      <path d="M150,360 C150,170 360,70 630,66 V360 Z" fill="var(--cyan)"/>
      <path d="M150,360 C150,170 360,70 630,66" fill="none" stroke="var(--silver)" stroke-width="7"/>
      <path d="M156,360 C156,176 362,76 630,72" fill="none" stroke="var(--silver-dark)" stroke-width="1.2" opacity="0.6"/>
    </svg>

    <div class="brand"><span class="brand-dot"></span><span>Crestline Floor<br>Inspections</span></div>
    <p class="tagline">ANALYSIS &amp; CONSULTING</p>
  </section>

</main>
</body>
</html>
```